Window and GutterCleaning Flyer A5 size double sided.

We need a double sided A5 flyer. Side 1, is for window cleaning, side 2 is for gutter cleaning. Licensed by Borough of Halvern Council.
Phone number 0800 315 4720.
Business address 7 Tarnlow Brae, North Pellin Edinburgh EH14 3RW.
www.clearpane-vista-services.com
We use a LoftPro Gutter inspection Cam to view your gutters first to see if they need doing.
Window cleaning ; Professional window cleaning services, what we offer, water fed pole window cleaning able to reach windows up to 60 feet.
Conservatory cleaning.
Conservatory roof cleaning.
Fascias & Soffits cleaning.
Excellent Customer Service.
Target Market(s)
domestic houses
Industry/Entity Type
window cleaning
Look and feel
Each slider illustrates characteristics of the customer's brand and the style your logo design should communicate.

```html
<!DOCTYPE html>
<html lang="en">
<head>
<meta charset="utf-8">
<title>Clearpane Vista – Window &amp; Gutter Cleaning Flyers</title>
<link rel="stylesheet" href="https://fonts.googleapis.com/css2?family=Poppins:ital,wght@0,400;0,500;0,600;0,700;0,800;1,400&display=swap">
<style>
  :root {
    --navy: #1d1657;
    --sky: #7fa9dd;
    --sky-soft: #a9cbef;
    --white: #ffffff;
    --page: #a6a6a6;
    --green: #2f7a3a;
    --photo-warm: #8a7a6a;
    --device: #2a2a2e;
  }
  * { box-sizing: border-box; margin: 0; padding: 0; }
  html, body { width: 1200px; height: 1117px; overflow: hidden; }
  body { background: var(--page); font-family: "Poppins", sans-serif; position: relative; }

  .flyer {
    position: absolute; top: 210px; width: 503px; height: 714px;
    background: var(--white); overflow: hidden;
  }
  .flyer--window { left: 79px; }
  .flyer--gutter { left: 617px; }

  .hero { position: absolute; left: 0; top: 0; width: 503px; height: 260px; }

  .title {
    position: absolute; left: 0; right: 0; top: 255px; text-align: center;
    font-weight: 800; font-size: 39px; line-height: 1; color: var(--navy); letter-spacing: -0.3px;
  }
  .title span { color: var(--sky); }
  .subtitle {
    position: absolute; left: 0; right: 0; top: 307px; text-align: center;
    font-weight: 600; font-size: 15.5px; line-height: 1.3; color: var(--navy);
  }
  .flyer--gutter .subtitle { font-size: 14px; top: 309px; }

  .offer-panel {
    position: absolute; left: 22px; top: 415px; width: 458px; height: 163px;
    background: var(--sky); border-radius: 16px;
  }
  .photo-strip { position: absolute; left: 38px; top: 361px; display: flex; }
  .photo-strip .frame {
    background: var(--white); padding: 3px; border-radius: 10px; margin-right: -1px;
  }
  .photo-strip .shot { width: 128px; height: 102px; border-radius: 8px; }
  .photo-strip .frame:nth-child(2) .shot { width: 160px; }
  .shot--conservatory { background: linear-gradient(160deg, #c9d6e4, #a06b4f); }
  .shot--pole { background: linear-gradient(160deg, #9fb7cf, #7a5f4c 60%, #d7dde2); }
  .shot--roof { background: linear-gradient(160deg, #cfd6dc, #8b8a6a); }

  .offer-heading {
    position: absolute; left: 60px; right: 60px; top: 483px;
    display: flex; align-items: center; gap: 12px;
    color: var(--white); font-weight: 600; font-size: 16.5px; white-space: nowrap;
  }
  .offer-heading::before, .offer-heading::after { content: ""; flex: 1; height: 1px; background: var(--white); }

  .offer-list { position: absolute; list-style: none; color: var(--white); font-size: 10.6px; line-height: 1.2; }
  .offer-list li { position: relative; padding-left: 13px; }
  .offer-list li svg { position: absolute; left: 0; top: 2px; }
  .offer-list--left { left: 64px; top: 508px; width: 220px; }
  .offer-list--left li:first-child { margin-bottom: 13px; }
  .offer-list--right { left: 281px; top: 508px; width: 200px; }
  .offer-list--right li { margin-bottom: 7px; }

  .contact-bar {
    position: absolute; left: 0; top: 587px; width: 366px; height: 116px;
    background: var(--navy); border-top-right-radius: 24px;
  }
  .phone {
    position: absolute; left: 44px; top: 600px; display: flex; align-items: center; gap: 6px;
    color: var(--sky); font-weight: 700; font-size: 34px; line-height: 1; letter-spacing: 0.3px;
  }
  .contact-line {
    position: absolute; left: 44px; display: flex; align-items: center; gap: 8px;
    color: var(--white); font-weight: 500; white-space: nowrap;
  }
  .contact-line--web { top: 644px; font-size: 13px; }
  .contact-line--address { top: 665px; font-size: 11px; }

  .bottom-strip { position: absolute; left: 0; top: 703px; width: 503px; height: 11px; display: flex; }
  .bottom-strip .white { width: 129px; background: var(--white); }
  .bottom-strip .navy { width: 9px; background: var(--navy); }
  .bottom-strip .sky { flex: 1; background: var(--sky-soft); }

  .brand {
    position: absolute; left: 376px; top: 606px; width: 110px;
    display: flex; flex-direction: column; align-items: center; gap: 6px;
  }
  .brand-square { width: 22px; height: 22px; background: var(--navy); }
  .brand-name { color: var(--navy); font-weight: 700; font-size: 14px; line-height: 1.15; text-align: center; }
  .licence {
    position: absolute; left: 372px; width: 118px; top: 686px; text-align: center;
    color: var(--navy); font-size: 5.2px; font-style: italic; white-space: nowrap;
  }

  .cam-panel {
    position: absolute; left: 53px; top: 513px; width: 410px; height: 65px;
    background: var(--sky); border-radius: 14px;
  }
  .cam-photo {
    position: absolute; left: 173px; top: 359px; width: 301px; height: 206px;
    border-radius: 20px; background: linear-gradient(135deg, #5f8a4a, #9bb07a 45%, #6d7074);
  }
  .cam-device {
    position: absolute; left: 22px; top: 365px; width: 193px; height: 222px;
    border-radius: 12px; background: linear-gradient(160deg, #3a3a40, var(--device));
  }
</style>
</head>
<body>

<section class="flyer flyer--window">
  <svg class="hero" viewBox="0 0 503 260">
    <path d="M0 140 Q 210 300 503 175 L503 195 Q 230 300 0 190 Z" fill="var(--sky-soft)"/>
    <path d="M0 105 Q 240 330 503 165 L503 0 L0 0 Z" fill="var(--navy)"/>
    <path d="M0 0 H503 V110 Q 250 290 0 115 Z" fill="var(--photo-warm)" role="img" aria-label="Photo of a cleaner using a water fed pole on a conservatory"/>
  </svg>

  <h1 class="title">WINDOW <span>CLEANING</span></h1>
  <p class="subtitle">We offer a high-quality, professional window<br>cleaning service across West Edinburgh.</p>

  <div class="offer-panel"></div>
  <div class="photo-strip">
    <div class="frame"><div class="shot shot--conservatory" role="img" aria-label="Photo of a clean conservatory"></div></div>
    <div class="frame"><div class="shot shot--pole" role="img" aria-label="Photo of a pole brush cleaning upper windows"></div></div>
    <div class="frame"><div class="shot shot--roof" role="img" aria-label="Photo of a conservatory roof being cleaned"></div></div>
  </div>

  <h2 class="offer-heading">WHAT WE OFFER</h2>
  <ul class="offer-list offer-list--left">
    <li><svg width="9" height="9" viewBox="0 0 10 10"><circle cx="5" cy="5" r="5" fill="#fff"/><path d="M2.8 5.2 4.4 6.7 7.3 3.6" stroke="var(--sky)" stroke-width="1.4" fill="none"/></svg>Water fed pole window cleaning<br>able to reach windows up to 60 feet.</li>
    <li><svg width="9" height="9" viewBox="0 0 10 10"><circle cx="5" cy="5" r="5" fill="#fff"/><path d="M2.8 5.2 4.4 6.7 7.3 3.6" stroke="var(--sky)" stroke-width="1.4" fill="none"/></svg>Conservatory cleaning.</li>
  </ul>
  <ul class="offer-list offer-list--right">
    <li><svg width="9" height="9" viewBox="0 0 10 10"><circle cx="5" cy="5" r="5" fill="#fff"/><path d="M2.8 5.2 4.4 6.7 7.3 3.6" stroke="var(--sky)" stroke-width="1.4" fill="none"/></svg>Conservatory roof cleaning.</li>
    <li><svg width="9" height="9" viewBox="0 0 10 10"><circle cx="5" cy="5" r="5" fill="#fff"/><path d="M2.8 5.2 4.4 6.7 7.3 3.6" stroke="var(--sky)" stroke-width="1.4" fill="none"/></svg>Fascias &amp; Soffits cleaning.</li>
    <li><svg width="9" height="9" viewBox="0 0 10 10"><circle cx="5" cy="5" r="5" fill="#fff"/><path d="M2.8 5.2 4.4 6.7 7.3 3.6" stroke="var(--sky)" stroke-width="1.4" fill="none"/></svg>Excellent Customer Service.</li>
  </ul>

  <div class="contact-bar"></div>
  <div class="phone"><svg width="22" height="28" viewBox="0 0 22 28"><path d="M5 1 L9 2 L10 8 L7 10 Q 9 17 14 21 L17 18 L21 21 L20 26 Q 14 28 8 21 Q 1 12 2 4 Z" fill="var(--sky)"/></svg>0800 315 4720</div>
  <div class="contact-line contact-line--web"><svg width="11" height="11" viewBox="0 0 12 12"><circle cx="6" cy="6" r="5.5" fill="var(--sky)"/><path d="M1 6H11M6 1Q3 6 6 11Q9 6 6 1" stroke="var(--navy)" stroke-width="0.8" fill="none"/></svg>www.clearpane-vista-services.com</div>
  <div class="contact-line contact-line--address"><svg width="10" height="13" viewBox="0 0 10 13"><path d="M5 0A5 5 0 0 1 10 5Q10 8 5 13Q0 8 0 5A5 5 0 0 1 5 0Z" fill="var(--sky)"/><circle cx="5" cy="5" r="1.8" fill="var(--navy)"/></svg>7 Tarnlow Brae, North Pellin Edinburgh EH14 3RW.</div>

  <div class="brand"><span class="brand-square"></span><span class="brand-name">Clearpane<br>Vista</span></div>
  <p class="licence">Licensed by Borough of Halvern Council.</p>

  <div class="bottom-strip"><span class="white"></span><span class="navy"></span><span class="sky"></span></div>
</section>

<section class="flyer flyer--gutter">
  <svg class="hero" viewBox="0 0 503 260">
    <path d="M0 140 Q 210 300 503 175 L503 195 Q 230 300 0 190 Z" fill="var(--sky-soft)"/>
    <path d="M0 105 Q 240 330 503 165 L503 0 L0 0 Z" fill="var(--navy)"/>
    <path d="M0 0 H503 V110 Q 250 290 0 115 Z" fill="#9a8f86" role="img" aria-label="Photo of a gutter vacuum hose at a roofline with fascia and soffit"/>
    <g font-family="Poppins, sans-serif" font-weight="600" font-size="16" fill="#fff" text-anchor="middle">
      <path d="M253 22 H336 V13 L354 34 L336 55 V46 H253 L246 34 Z" fill="var(--green)"/>
      <text x="296" y="40">Gutter</text>
      <path d="M220 78 H303 V69 L321 90 L303 111 V102 H220 L213 90 Z" fill="var(--green)"/>
      <text x="263" y="96">Fascia</text>
      <path d="M187 141 H270 V132 L288 153 L270 174 V165 H187 L180 153 Z" fill="var(--green)"/>
      <text x="228" y="159">Soffit</text>
    </g>
  </svg>

  <h1 class="title">GUTTER <span>CLEANING</span></h1>
  <p class="subtitle">We use a LoftPro Gutter inspection Cam<br>to view your gutters first to see if they need doing.</p>

  <div class="cam-panel"></div>
  <div class="cam-photo" role="img" aria-label="Photo of a carbon gutter vacuum pole with camera on a roof edge"></div>
  <div class="cam-device" role="img" aria-label="Photo of the gutter inspection camera monitor and camera head"></div>

  <div class="contact-bar"></div>
  <div class="phone"><svg width="22" height="28" viewBox="0 0 22 28"><path d="M5 1 L9 2 L10 8 L7 10 Q 9 17 14 21 L17 18 L21 21 L20 26 Q 14 28 8 21 Q 1 12 2 4 Z" fill="var(--sky)"/></svg>0800 315 4720</div>
  <div class="contact-line contact-line--web"><svg width="11" height="11" viewBox="0 0 12 12"><circle cx="6" cy="6" r="5.5" fill="var(--sky)"/><path d="M1 6H11M6 1Q3 6 6 11Q9 6 6 1" stroke="var(--navy)" stroke-width="0.8" fill="none"/></svg>www.clearpane-vista-services.com</div>
  <div class="contact-line contact-line--address"><svg width="10" height="13" viewBox="0 0 10 13"><path d="M5 0A5 5 0 0 1 10 5Q10 8 5 13Q0 8 0 5A5 5 0 0 1 5 0Z" fill="var(--sky)"/><circle cx="5" cy="5" r="1.8" fill="var(--navy)"/></svg>7 Tarnlow Brae, North Pellin Edinburgh EH14 3RW.</div>

  <div class="brand"><span class="brand-square"></span><span class="brand-name">Clearpane<br>Vista</span></div>
  <p class="licence">Licensed by Borough of Halvern Council.</p>

  <div class="bottom-strip"><span class="white"></span><span class="navy"></span><span class="sky"></span></div>
</section>

</body>
</html>
```